New Look and Feel for 82 year old Varrenko Ltd. presentations

We are seeking new ideas to have powerpoint-layouts for the group headquarters. Varrenko is an industrial company in maritime, hydraulics, heavy machinery and industrial services. Please read our history and watch the video for a quick familiarization. http://www.varrenko-example.fi/eng/main.php

Our customer relationships are based on trust, with Varrenko providing to customers, cooperation partners and other interest groups products and solutions that produce sustainable benefits.

Varrenko strives to ensure that the environmental impact of the products is considered over the entire life cycle and the processes used by the Group are as environmentally benign as possible.

Industry/Entity Type

It Company

Colors

Designer to choose colors to be used in the design.

Requirements
Must have
• Logo
Nice to have
• example animations and transitions

```html
<!DOCTYPE html>
<html lang="en">
<head>
<meta charset="utf-8">
<title>Varrenko Business Group – Presentation Layouts</title>
<link href="https://fonts.googleapis.com/css2?family=Ubuntu:wght@300;400;500;700&display=swap" rel="stylesheet">
<style>
:root{
  --red:#e8403f;
  --red-dark:#c9302f;
  --ink:#2a2a2d;
  --text:#4a4a4a;
  --muted:#8a8a8a;
  --line:#e3e3e3;
  --paper:#ffffff;
  --strip:#4b4b4d;
}
*{box-sizing:border-box;margin:0;padding:0}
html,body{width:1200px;height:1200px;overflow:hidden;background:var(--paper)}
body{font-family:"Ubuntu",sans-serif;color:var(--text);position:relative}
.slide{position:absolute;width:300px;height:168px;overflow:hidden;background:var(--paper)}
.wide{width:600px;height:336px}
.abs{position:absolute}
.ph{position:absolute}
.ph-steel{background:linear-gradient(135deg,#3d5a78,#9fb3c6 45%,#d9d4c8 70%,#5b6b7a)}
.ph-ind{background:linear-gradient(135deg,#24364d,#c9862d 40%,#e2e6ea 65%,#3a4a5e)}
.ph-sea{background:linear-gradient(180deg,#2d5fa0,#7fb0de 45%,#f0f2f4 62%,#b53a2c 85%,#2a2a2a)}
.ph-red{background:linear-gradient(135deg,#e8403f,#f06a5c 50%,#c9302f)}
.ph-green{background:linear-gradient(135deg,#1d1d1d,#3f6b22 50%,#1c1c1c)}
.ph-dark{background:linear-gradient(135deg,#1f2c3d,#5c6f84 50%,#202a36)}
.ph-soil{background:linear-gradient(135deg,#3a2a1e,#6f5038 50%,#4d8a2c)}
.h-title{font-weight:700;color:var(--ink);font-size:8px;text-align:center}
.h-sub{font-size:3.4px;color:var(--muted);text-align:center;margin-top:1px}
.tiny{font-size:3.2px;line-height:1.35;color:var(--muted)}
.label{font-size:5px;font-weight:700;color:var(--ink)}
.footer{position:absolute;left:0;right:0;bottom:0;height:8px;border-top:1px solid var(--red);font-size:3px;color:var(--muted);display:flex;justify-content:space-between;align-items:center;padding:0 4px}
.footer .brand{font-weight:700;color:var(--ink);display:flex;align-items:center;gap:2px}
.footer .brand i{display:inline-block;width:4px;height:4px;background:var(--red)}
.btn{position:absolute;background:var(--red);color:#fff;font-size:3.2px;text-align:center;padding:1.5px 0}
.icon{position:absolute;width:16px;height:16px}
.card{position:absolute;background:#fff;border:1px solid var(--line)}
.num{font-size:20px;font-weight:700;color:var(--red)}
.strip{position:absolute;left:0;top:1176px;width:1200px;height:24px;background:var(--strip)}
</style>
</head>
<body>

<!-- Cover -->
<section class="slide wide" style="left:0;top:0">
  <div class="abs" style="left:24px;top:118px;font-size:25px;font-weight:300;color:var(--ink)">Varrenko</div>
  <div class="abs" style="left:24px;top:144px;font-size:27px;font-weight:700;color:var(--ink)">Business Group</div>
  <div class="abs" style="left:24px;top:178px;font-size:10px;color:var(--text)">FI-26100 Kestola</div>
  <div class="abs" style="left:24px;top:199px;font-size:10px;color:var(--text);display:flex;align-items:center;gap:4px">
    <svg width="10" height="10" viewBox="0 0 10 10"><rect x="0.5" y="1.5" width="9" height="8" fill="none" stroke="#4a4a4a"/><line x1="0.5" y1="3.5" x2="9.5" y2="3.5" stroke="#4a4a4a"/></svg>
    15<sup style="font-size:5px">TH</sup> DEC 2017 | Finland
  </div>
  <svg class="abs" style="left:150px;top:0" width="450" height="336" viewBox="0 0 450 336">
    <g stroke="#e8403f" stroke-width="1.2">
      <polygon points="150,0 210,0 160,70 115,20" fill="#5a4a3a" role="img" aria-label="Harbour at dusk"/>
      <polygon points="290,0 380,0 330,60 270,20" fill="#3d5a78" role="img" aria-label="Industrial site photograph"/>
      <polygon points="300,-30 449,0 449,100 360,120 290,50" fill="#6f5038" role="img" aria-label="Seedling in soil held in hands"/>
      <polygon points="300,10 420,130 300,250 180,130" fill="url(#g1)" role="img" aria-label="Industrial pipework photograph"/>
      <polygon points="130,150 240,260 130,370 20,260" fill="url(#g2)" role="img" aria-label="Ship sailing through waves"/>
      <polygon points="420,150 449,180 449,336 330,336 330,240" fill="url(#g3)" role="img" aria-label="Engineer working at machinery"/>
      <polygon points="260,270 330,336 190,336" fill="#2c3e55" role="img" aria-label="Factory building"/>
      <polygon points="20,285 60,336 -20,336" fill="#33475e" role="img" aria-label="Port cranes"/>
      <polygon points="449,100 449,150 425,125" fill="#2d4fa0"/>
    </g>
    <defs>
      <linearGradient id="g1" x1="0" y1="0" x2="1" y2="1"><stop offset="0" stop-color="#2b5aa8"/><stop offset=".45" stop-color="#c9c9c4"/><stop offset=".75" stop-color="#d8b43a"/><stop offset="1" stop-color="#5c6d82"/></linearGradient>
      <linearGradient id="g2" x1="0" y1="0" x2="0" y2="1"><stop offset="0" stop-color="#2d5fa0"/><stop offset=".4" stop-color="#9fc4e6"/><stop offset=".55" stop-color="#f0f2f4"/><stop offset=".8" stop-color="#b53a2c"/><stop offset="1" stop-color="#1d2a3a"/></linearGradient>
      <linearGradient id="g3" x1="0" y1="0" x2="1" y2="1"><stop offset="0" stop-color="#9aa5ad"/><stop offset=".5" stop-color="#e1e4e6"/><stop offset="1" stop-color="#c97a3a"/></linearGradient>
    </defs>
  </svg>
</section>

<!-- Why choose -->
<section class="slide wide" style="left:600px;top:0">
  <svg class="abs" style="left:0;top:0" width="600" height="336" viewBox="0 0 600 336">
    <polygon points="0,0 425,0 140,290 0,150" fill="#e8403f"/>
    <polygon points="0,168 140,168 245,265 175,336 0,336" fill="#2a2a2d"/>
    <polygon points="240,60 330,140 240,230 150,140" fill="url(#g4)" stroke="#fff" stroke-width="3" role="img" aria-label="Engineer among industrial equipment"/>
    <defs><linearGradient id="g4" x1="0" y1="0" x2="1" y2="1"><stop offset="0" stop-color="#2d4a6a"/><stop offset=".5" stop-color="#7fa9c8"/><stop offset=".7" stop-color="#b6d23a"/><stop offset="1" stop-color="#3a4a5e"/></linearGradient></defs>
  </svg>
  <div class="abs" style="left:10px;top:264px;font-size:11px;font-weight:500;color:#fff">Lorem Ipsum</div>
  <div class="abs" style="left:10px;top:278px;font-size:7px;line-height:1.35;color:#ddd;width:100px">Lorem ipsum dolor sit amet, consectetur adipiscing elit, sed do eiusmod tempor.</div>
  <div class="abs" style="left:376px;top:128px;background:var(--red);color:#fff;font-size:7px;padding:1px 8px">WHY CHOOSE</div>
  <div class="abs" style="left:376px;top:142px;font-size:22px;font-weight:700;color:var(--ink)">VARRENKO ?</div>
  <div class="abs" style="left:378px;top:174px;width:180px;font-size:7.4px;line-height:1.3;color:var(--text)">Lorem ipsum dolor sit amet, consectetur adipiscing elit, sed do eiusmod tempor incididunt ut labore et dolore magna aliqua. Ut enim ad minim veniam, quis nostrud exercitation ullamco laboris nisi ut aliquip ex ea commodo consequat.</div>
  <div class="btn" style="left:379px;top:230px;width:70px;font-size:6px;padding:5px 0">FIND MORE</div>
</section>

<!-- Row 2 -->
<section class="slide" style="left:0;top:336px">
  <div class="ph ph-dark" style="inset:0" role="img" aria-label="Two engineers inspecting gear machinery"></div>
  <svg class="abs" style="left:0;top:0" width="300" height="168"><polygon points="0,30 110,168 0,168" fill="#e8403f"/></svg>
  <div class="abs" style="left:8px;top:97px;color:#fff;font-size:4px;font-weight:700">CASE STUDY</div>
  <div class="abs" style="left:8px;top:102px;color:#fff;font-size:3.5px">2017 - 2018</div>
  <div class="abs" style="left:8px;top:112px;color:#fff;font-size:5px;font-weight:700">Lorem ipsum</div>
  <div class="abs" style="left:8px;top:119px;color:#fff;font-size:3.4px;width:60px;line-height:1.3">Lorem ipsum dolor sit amet, consectetur adipiscing elit, sed do eiusmod</div>
</section>

<section class="slide" style="left:300px;top:336px">
  <svg class="abs" style="left:0;top:0" width="150" height="168">
    <polygon points="0,0 70,0 0,70" fill="#e8403f"/>
    <polygon points="0,135 30,168 0,168" fill="#e8403f"/>
    <polygon points="70,30 90,50 70,70 50,50" fill="#2a2a2d"/>
    <polygon points="65,108 77,120 65,132 53,120" fill="#2a2a2d"/>
    <polygon points="45,50 85,90 45,130 5,90" fill="#c97a3a" stroke="#fff" stroke-width="2" role="img" aria-label="Offshore platform photograph"/>
  </svg>
  <div class="abs" style="left:6px;top:143px;background:var(--red);color:#fff;font-size:2.8px;padding:1px 3px">Year 2018</div>
  <div class="abs" style="left:6px;top:151px;font-size:9px;font-weight:700;color:var(--ink)">AGENDA</div>
  <div class="abs" style="left:150px;top:24px;font-size:9px;font-weight:500;color:var(--ink)">AGENDA</div>
  <table class="abs" style="left:150px;top:40px;width:114px;border-collapse:collapse;font-size:3px;color:var(--muted)">
    <tr><td style="border-bottom:1px solid var(--line);padding:2px">Introduction</td><td style="text-align:right">2</td></tr>
    <tr><td style="border-bottom:1px solid var(--line);padding:2px">About Us</td><td style="text-align:right">4</td></tr>
    <tr><td style="border-bottom:1px solid var(--line);padding:2px">Timeline</td><td style="text-align:right">6</td></tr>
    <tr><td style="border-bottom:1px solid var(--line);padding:2px">Milestone</td><td style="text-align:right">8</td></tr>
    <tr><td style="border-bottom:1px solid var(--line);padding:2px">Perspective Points</td><td style="text-align:right">10</td></tr>
    <tr><td style="border-bottom:1px solid var(--line);padding:2px">Portfolio</td><td style="text-align:right">12</td></tr>
    <tr><td style="border-bottom:1px solid var(--line);padding:2px">Meet Our Team</td><td style="text-align:right">14</td></tr>
    <tr><td style="border-bottom:1px solid var(--line);padding:2px">Infographic Contents</td><td style="text-align:right">16</td></tr>
    <tr><td style="border-bottom:1px solid var(--line);padding:2px">Creative Slides</td><td style="text-align:right">18</td></tr>
    <tr><td style="border-bottom:1px solid var(--line);padding:2px">Contact Us</td><td style="text-align:right">20</td></tr>
  </table>
</section>

<section class="slide" style="left:600px;top:336px">
  <svg class="abs" style="left:80px;top:14px" width="140" height="72">
    <polygon points="70,2 95,27 70,52 45,27" fill="#e8403f" stroke="#2a2a2d" stroke-width="1" role="img" aria-label="Gear illustration on red"/>
    <polygon points="30,30 55,55 30,80 5,55" fill="#3a3f6a" stroke="#2a2a2d" stroke-width="1" role="img" aria-label="Harbour at sunset"/>
    <polygon points="110,30 135,55 110,80 85,55" fill="#8aa03a" stroke="#2a2a2d" stroke-width="1" role="img" aria-label="Industrial plant"/>
  </svg>
  <div class="abs" style="left:137px;top:78px;background:var(--red);color:#fff;font-size:2.6px;padding:0.5px 2px">WHY CHOOSE</div>
  <div class="abs" style="left:127px;top:85px;font-size:8px;font-weight:700;color:var(--ink)">VARRENKO</div>
  <div class="abs" style="left:55px;top:120px;width:50px"><svg width="12" height="12"><rect x="1" y="2" width="10" height="8" fill="none" stroke="#e8403f"/></svg><div class="label" style="font-size:4.4px">Lorem Ipsum</div><div class="tiny" style="font-size:2.8px">Lorem ipsum dolor sit amet, consectetur adipiscing elit, sed do eiusmod tempor</div></div>
  <div class="abs" style="left:128px;top:120px;width:50px"><svg width="12" height="12"><circle cx="6" cy="6" r="4.5" fill="none" stroke="#e8403f"/></svg><div class="label" style="font-size:4.4px">Lorem Ipsum</div><div class="tiny" style="font-size:2.8px">Lorem ipsum dolor sit amet, consectetur adipiscing elit, sed do eiusmod tempor</div></div>
  <div class="abs" style="left:201px;top:120px;width:50px"><svg width="12" height="12"><rect x="3" y="1" width="6" height="10" fill="none" stroke="#e8403f"/></svg><div class="label" style="font-size:4.4px">Lorem Ipsum</div><div class="tiny" style="font-size:2.8px">Lorem ipsum dolor sit amet, consectetur adipiscing elit, sed do eiusmod tempor</div></div>
</section>

<section class="slide" style="left:900px;top:336px">
  <div class="ph ph-red" style="left:150px;top:0;width:150px;height:160px" role="img" aria-label="Industrial plant with red overlay"></div>
  <svg class="abs" style="left:213px;top:67px" width="24" height="24"><polygon points="2,12 22,3 15,22 11,14" fill="none" stroke="#fff" stroke-width="1.2"/></svg>
  <div class="abs" style="left:27px;top:38px;font-size:14px;font-weight:700;color:var(--ink)">WELCOME</div>
  <div class="abs" style="left:27px;top:55px;font-size:6px;color:var(--text)">MESSAGE</div>
  <div class="abs tiny" style="left:27px;top:76px;width:80px">Lorem ipsum dolor sit amet, consectetur adipiscing elit, sed do eiusmod tempor incididunt ut labore et dolore magna aliqua.</div>
  <div class="abs tiny" style="left:27px;top:100px;width:80px">Duis aute irure dolor in reprehenderit in voluptate velit esse cillum dolore eu fugiat nulla pariatur. Excepteur sint occaecat cupidatat non proident, sunt in culpa qui officia deserunt mollit.</div>
  <div class="footer"><span class="brand"><i></i>VARRENKO</span><span>varrenko-example.fi</span><span>FRIDAY, DEC 15TH 2017</span></div>
</section>

<!-- Row 3 -->
<section class="slide" style="left:0;top:504px">
  <div class="abs" style="left:25px;top:22px;display:flex;align-items:center;gap:3px"><i style="display:inline-block;width:8px;height:8px;background:var(--red)"></i><span style="font-size:6px;font-weight:700;color:var(--ink)">Varrenko</span></div>
  <div class="abs" style="left:25px;top:44px;font-size:15px;font-weight:300;color:var(--ink)">About</div>
  <div class="abs" style="left:25px;top:62px;font-size:14px;font-weight:700;color:var(--ink)">VARRENKO</div>
  <div class="abs" style="left:25px;top:80px;font-size:8px;color:var(--text)">Engineering Works</div>
  <div class="abs" style="left:23px;top:112px;width:78px;display:flex;gap:3px"><svg width="18" height="18"><circle cx="9" cy="9" r="8" fill="none" stroke="#2a2a2d"/><circle cx="9" cy="7" r="3" fill="none" stroke="#e8403f"/></svg><div><div class="label" style="font-size:4.5px">Team Support</div><div class="tiny" style="font-size:2.8px">Lorem ipsum dolor sit amet, consectetur adipiscing elit, sed do eiusmod</div></div></div>
  <div class="abs" style="left:116px;top:112px;width:78px;display:flex;gap:3px"><svg width="18" height="18"><rect x="5" y="2" width="8" height="14" fill="none" stroke="#e8403f"/></svg><div><div class="label" style="font-size:4.5px">Achiever</div><div class="tiny" style="font-size:2.8px">Lorem ipsum dolor sit amet, consectetur adipiscing elit, sed do eiusmod</div></div></div>
  <div class="abs" style="left:208px;top:112px;width:78px;display:flex;gap:3px"><svg width="18" height="18"><polyline points="2,16 9,4 16,16" fill="none" stroke="#2a2a2d"/><circle cx="9" cy="4" r="2" fill="#e8403f"/></svg><div><div class="label" style="font-size:4.5px">Goals</div><div class="tiny" style="font-size:2.8px">Lorem ipsum dolor sit amet, consectetur adipiscing elit, sed do eiusmod</div></div></div>
  <div class="footer"><span class="brand"><i></i>VARRENKO</span><span>varrenko-example.fi</span><span>FRIDAY, DEC 15TH 2017</span></div>
</section>

<section class="slide" style="left:300px;top:504px">
  <div class="abs" style="left:0;top:0;width:300px;height:84px;background:var(--red)"></div>
  <div class="abs" style="left:0;top:30px;width:300px;text-align:center;color:#fff;font-size:9px;font-weight:700">About Us</div>
  <div class="abs" style="left:0;top:45px;width:300px;text-align:center;color:#fde;font-size:3.4px">Energy &amp; Environment – Engineering Works</div>
  <div class="abs" style="left:0;top:97px;width:300px;text-align:center;font-size:7px;color:var(--ink)">WE ARE <b>VARRENKO</b> WORKS</div>
  <div class="abs tiny" style="left:70px;top:112px;width:160px;text-align:center">Lorem ipsum dolor sit amet, consectetur adipiscing elit, sed do eiusmod tempor incididunt ut labore et dolore magna aliqua.</div>
  <div class="abs tiny" style="left:70px;top:126px;width:160px;text-align:center">Duis aute irure dolor in reprehenderit in voluptate velit esse cillum dolore eu fugiat nulla pariatur. Excepteur sint occaecat cupidatat non proident, sunt in culpa qui officia deserunt mollit.</div>
  <div class="footer"><span class="brand"><i></i>VARRENKO</span><span>varrenko-example.fi</span><span>FRIDAY, DEC 15TH 2017</span></div>
</section>

<section class="slide" style="left:600px;top:504px">
  <div class="abs h-title" style="left:0;top:14px;width:300px;font-size:6.5px">Company History</div>
  <div class="abs h-sub" style="left:0;top:22px;width:300px">Your Subtitle Goes Here</div>
  <svg class="abs" style="left:15px;top:70px" width="270" height="60" viewBox="0 0 270 60">
    <g fill="none" stroke="#2a2a2d" stroke-width="0.8">
      <polyline points="0,20 10,30 0,40"/><polyline points="5,20 15,30 5,40"/>
      <polyline points="15,30 30,30 30,10 55,10 55,40 85,40 85,10 115,10 115,40 145,40 145,10 175,10 175,40 205,40 205,10 240,10 240,30 255,30"/>
      <polyline points="250,20 260,30 250,40"/><polyline points="255,20 265,30 255,40"/>
    </g>
    <g fill="#e8403f"><ellipse cx="53" cy="10" rx="6" ry="3"/><ellipse cx="145" cy="10" rx="6" ry="3"/><ellipse cx="237" cy="10" rx="6" ry="3"/><ellipse cx="100" cy="40" rx="6" ry="3"/><ellipse cx="190" cy="40" rx="6" ry="3"/></g>
    <g fill="none" stroke="#e8403f" stroke-width="0.8"><circle cx="52" cy="24" r="4"/><rect x="95" y="20" width="8" height="8"/><circle cx="145" cy="24" r="4"/><rect x="184" y="20" width="8" height="8"/><circle cx="231" cy="24" r="4"/></g>
  </svg>
  <div class="abs label" style="left:48px;top:101px;font-size:3.8px">Lorem ipsum</div>
  <div class="abs label" style="left:94px;top:101px;font-size:3.8px">Lorem ipsum</div>
  <div class="abs label" style="left:138px;top:101px;font-size:3.8px">Lorem ipsum</div>
  <div class="abs label" style="left:182px;top:101px;font-size:3.8px">Lorem ipsum</div>
  <div class="abs label" style="left:226px;top:101px;font-size:3.8px">Lorem ipsum</div>
  <div class="abs" style="left:48px;top:36px;width:55px"><div class="label" style="font-size:4px">Lorem ipsum</div><div class="tiny" style="font-size:2.8px">Lorem ipsum dolor sit amet, consectetur adipiscing elit, sed do eiusmod</div></div>
  <div class="abs" style="left:140px;top:36px;width:55px"><div class="label" style="font-size:4px">Lorem ipsum</div><div class="tiny" style="font-size:2.8px">Lorem ipsum dolor sit amet, consectetur adipiscing elit, sed do eiusmod</div></div>
  <div class="abs" style="left:228px;top:36px;width:55px"><div class="label" style="font-size:4px">Lorem ipsum</div><div class="tiny" style="font-size:2.8px">Lorem ipsum dolor sit amet, consectetur adipiscing elit, sed do eiusmod</div></div>
  <div class="abs" style="left:91px;top:132px;width:55px"><div class="label" style="font-size:4px">Lorem ipsum</div><div class="tiny" style="font-size:2.8px">Lorem ipsum dolor sit amet, consectetur adipiscing elit, sed do eiusmod</div></div>
  <div class="abs" style="left:181px;top:132px;width:55px"><div class="label" style="font-size:4px">Lorem ipsum</div><div class="tiny" style="font-size:2.8px">Lorem ipsum dolor sit amet, consectetur adipiscing elit, sed do eiusmod</div></div>
</section>

<section class="slide" style="left:900px;top:504px">
  <div class="abs h-title" style="left:0;top:14px;width:300px;font-size:11px">Our Mission</div>
  <div class="abs" style="left:0;top:31px;width:300px;text-align:center;font-size:5px;color:var(--muted)">Business Heights</div>
  <div class="abs" style="left:27px;top:62px;width:70px"><div class="label" style="font-size:6px">Environment</div><div class="tiny" style="font-size:2.8px">Lorem ipsum dolor sit amet</div><div class="tiny" style="font-size:2.8px;margin-top:6px">Lorem ipsum dolor sit amet, consectetur adipiscing elit, sed do eiusmod tempor incididunt ut labore et dolore magna aliqua.</div></div>
  <div class="abs" style="left:118px;top:62px;width:70px"><div class="label" style="font-size:6px">Flexible</div><div class="tiny" style="font-size:2.8px">Lorem ipsum dolor sit amet</div><div class="tiny" style="font-size:2.8px;margin-top:6px">Lorem ipsum dolor sit amet, consectetur adipiscing elit, sed do eiusmod tempor incididunt ut labore et dolore magna aliqua.</div></div>
  <div class="abs" style="left:208px;top:62px;width:70px"><div class="label" style="font-size:6px">Loyalty</div><div class="tiny" style="font-size:2.8px">Lorem ipsum dolor sit amet</div><div class="tiny" style="font-size:2.8px;margin-top:6px">Lorem ipsum dolor sit amet, consectetur adipiscing elit, sed do eiusmod tempor incididunt ut labore et dolore magna aliqua.</div></div>
  <div class="btn" style="left:28px;top:108px;width:40px">Read More</div>
  <div class="btn" style="left:119px;top:108px;width:40px">Read More</div>
  <div class="btn" style="left:209px;top:108px;width:40px">Read More</div>
  <div class="abs tiny" style="left:70px;top:136px;width:160px;text-align:center">Duis aute irure dolor in reprehenderit in voluptate velit esse cillum dolore eu fugiat nulla pariatur. Excepteur sint occaecat cupidatat non proident, sunt in culpa qui officia deserunt mollit.</div>
  <div class="footer"><span class="brand"><i></i>VARRENKO</span><span>varrenko-example.fi</span><span>FRIDAY, DEC 15TH 2017</span></div>
</section>

<!-- Row 4 -->
<section class="slide" style="left:0;top:672px">
  <div class="abs h-title" style="left:0;top:14px;width:300px">Implementation</div>
  <div class="abs h-sub" style="left:0;top:24px;width:300px;font-size:4px">of sustainable development</div>
  <svg class="abs" style="left:58px;top:50px" width="30" height="30"><circle cx="15" cy="15" r="13" fill="none" stroke="#ddd"/><circle cx="15" cy="15" r="8" fill="#e8403f"/></svg>
  <svg class="abs" style="left:134px;top:50px" width="30" height="30"><circle cx="15" cy="15" r="13" fill="none" stroke="#ddd"/><circle cx="15" cy="15" r="8" fill="none" stroke="#e8403f" stroke-width="2"/></svg>
  <svg class="abs" style="left:210px;top:50px" width="30" height="30"><circle cx="15" cy="15" r="13" fill="none" stroke="#ddd"/><circle cx="15" cy="15" r="8" fill="#e8403f"/><circle cx="15" cy="15" r="3" fill="#fff"/></svg>
  <div class="abs" style="left:43px;top:91px;width:60px;text-align:center"><div class="label" style="font-size:5px">Environment</div><div class="tiny" style="font-size:2.8px;margin-top:6px">Lorem ipsum dolor sit amet, consectetur adipiscing elit, sed do eiusmod</div></div>
  <div class="abs" style="left:119px;top:91px;width:60px;text-align:center"><div class="label" style="font-size:5px">Strategy</div><div class="tiny" style="font-size:2.8px;margin-top:6px">Lorem ipsum dolor sit amet, consectetur adipiscing elit, sed do eiusmod</div></div>
  <div class="abs" style="left:195px;top:91px;width:60px;text-align:center"><div class="label" style="font-size:5px">Industrial</div><div class="tiny" style="font-size:2.8px;margin-top:6px">Lorem ipsum dolor sit amet, consectetur adipiscing elit, sed do eiusmod</div></div>
  <div class="footer"><span class="brand"><i></i>VARRENKO</span><span>varrenko-example.fi</span><span>FRIDAY, DEC 15TH 2017</span></div>
</section>

<section class="slide" style="left:300px;top:672px">
  <div class="abs h-title" style="left:0;top:14px;width:300px">Our Vision</div>
  <div class="abs h-sub" style="left:0;top:24px;width:300px;font-size:4px">From experienced professionals</div>
  <div class="card" style="left:25px;top:41px;width:250px;height:80px"></div>
  <div class="abs" style="left:108px;top:41px;width:1px;height:80px;background:var(--line)"></div>
  <div class="abs" style="left:191px;top:41px;width:1px;height:80px;background:var(--line)"></div>
  <div class="abs" style="left:36px;top:52px;width:64px"><svg width="16" height="16"><circle cx="8" cy="8" r="6" fill="none" stroke="#e8403f"/></svg><div class="label" style="font-size:6.5px;font-weight:500">Hydraulics</div><div class="tiny" style="font-size:2.8px;margin-top:3px">Lorem ipsum dolor sit amet, consectetur adipiscing elit,</div><div class="tiny" style="font-size:2.8px;margin-top:3px;color:var(--ink)">Learn More</div></div>
  <div class="abs" style="left:119px;top:52px;width:64px"><svg width="16" height="16"><polygon points="8,1 14,14 2,14" fill="none" stroke="#e8403f"/></svg><div class="label" style="font-size:6.5px;font-weight:500">Implement</div><div class="tiny" style="font-size:2.8px;margin-top:3px">Lorem ipsum dolor sit amet, consectetur adipiscing elit,</div><div class="tiny" style="font-size:2.8px;margin-top:3px;color:var(--ink)">Learn More</div></div>
  <div class="abs" style="left:202px;top:52px;width:64px"><svg width="16" height="16"><rect x="3" y="1" width="10" height="14" fill="none" stroke="#e8403f"/></svg><div class="label" style="font-size:6.5px;font-weight:500">Readiness</div><div class="tiny" style="font-size:2.8px;margin-top:3px">Lorem ipsum dolor sit amet, consectetur adipiscing elit,</div><div class="tiny" style="font-size:2.8px;margin-top:3px;color:var(--ink)">Learn More</div></div>
  <div class="abs tiny" style="left:70px;top:132px;width:160px;text-align:center">Duis aute irure dolor in reprehenderit in voluptate velit esse cillum dolore eu fugiat nulla pariatur. Excepteur sint occaecat cupidatat non proident, sunt in culpa qui officia deserunt mollit.</div>
  <div class="footer"><span class="brand"><i></i>VARRENKO</span><span>varrenko-example.fi</span><span>FRIDAY, DEC 15TH 2017</span></div>
</section>

<section class="slide" style="left:600px;top:672px">
  <div class="ph ph-steel" style="left:140px;top:0;width:160px;height:160px" role="img" aria-label="Industrial pipework photograph"></div>
  <div class="abs num" style="left:18px;top:30px">01</div>
  <div class="abs" style="left:48px;top:33px;width:80px"><div class="label" style="font-size:7px;font-weight:500">Our Mission</div><div class="tiny" style="font-size:2.8px">Lorem ipsum dolor sit amet, consectetur adipiscing elit, sed do eiusmod</div></div>
  <div class="abs num" style="left:18px;top:68px">02</div>
  <div class="abs" style="left:48px;top:71px;width:80px"><div class="label" style="font-size:7px;font-weight:500">Our Vision</div><div class="tiny" style="font-size:2.8px">Lorem ipsum dolor sit amet, consectetur adipiscing elit, sed do eiusmod</div></div>
  <div class="abs num" style="left:18px;top:106px">03</div>
  <div class="abs" style="left:48px;top:109px;width:80px"><div class="label" style="font-size:7px;font-weight:500">Our Values</div><div class="tiny" style="font-size:2.8px">Lorem ipsum dolor sit amet, consectetur adipiscing elit, sed do eiusmod</div></div>
  <div class="footer"><span class="brand"><i></i>VARRENKO</span><span>varrenko-example.fi</span><span>FRIDAY, DEC 15TH 2017</span></div>
</section>

<section class="slide" style="left:900px;top:672px">
  <div class="abs h-title" style="left:0;top:14px;width:300px;font-size:6.5px">Our Main Products</div>
  <div class="abs h-sub" style="left:0;top:22px;width:300px">Your Subtitle Goes Here</div>
  <div class="abs" style="left:67px;top:36px;font-size:3px;color:var(--muted)">OUR</div>
  <div class="abs" style="left:67px;top:40px;font-size:8px;font-weight:500;color:var(--ink)">PRODUCTS</div>
  <div class="abs" style="left:45px;top:60px;display:flex;gap:4px;width:80px"><svg width="16" height="14"><rect x="1" y="3" width="14" height="9" fill="none" stroke="#e8403f"/></svg><div><div class="label" style="font-size:4.4px;font-weight:500">Lorem ipsum</div><div class="tiny" style="font-size:2.6px">Lorem ipsum dolor sit amet, consectetur adipiscing elit, sed do eiusmod</div></div></div>
  <div class="abs" style="left:45px;top:88px;display:flex;gap:4px;width:80px"><svg width="16" height="14"><rect x="3" y="1" width="10" height="12" fill="none" stroke="#e8403f"/></svg><div><div class="label" style="font-size:4.4px;font-weight:500">Lorem ipsum</div><div class="tiny" style="font-size:2.6px">Lorem ipsum dolor sit amet, consectetur adipiscing elit, sed do eiusmod</div></div></div>
  <div class="abs" style="left:45px;top:116px;display:flex;gap:4px;width:80px"><svg width="16" height="14"><circle cx="8" cy="7" r="5" fill="none" stroke="#e8403f"/></svg><div><div class="label" style="font-size:4.4px;font-weight:500">Lorem ipsum</div><div class="tiny" style="font-size:2.6px">Lorem ipsum dolor sit amet, consectetur adipiscing elit, sed do eiusmod</div></div></div>
  <div class="ph ph-sea" style="left:138px;top:37px;width:53px;height:88px" role="img" aria-label="Marine vessel product photo"></div>
  <div class="ph ph-ind" style="left:192px;top:37px;width:53px;height:88px" role="img" aria-label="Technical machinery product photo"></div>
  <div class="ph ph-steel" style="left:246px;top:37px;width:54px;height:88px" role="img" aria-label="Auxiliary equipment product photo"></div>
  <div class="abs" style="left:138px;top:125px;width:53px;background:var(--red);color:#fff;font-size:3px;text-align:center;padding:1px 0">NORDMARINE</div>
  <div class="abs" style="left:192px;top:125px;width:53px;background:var(--ink);color:#fff;font-size:3px;text-align:center;padding:1px 0">KALTECH</div>
  <div class="abs" style="left:246px;top:125px;width:54px;background:var(--red);color:#fff;font-size:3px;text-align:center;padding:1px 0">AUXILIARY</div>
  <div class="footer"><span class="brand"><i></i>VARRENKO</span><span>varrenko-example.fi</span><span>FRIDAY, DEC 15TH 2017</span></div>
</section>

<!-- Row 5 -->
<section class="slide" style="left:0;top:840px">
  <div class="abs h-title" style="left:0;top:14px;width:300px">Our Major Services</div>
  <div class="abs h-sub" style="left:0;top:24px;width:300px">Your Subtitle Goes Here</div>
  <div class="ph ph-steel" style="left:20px;top:40px;width:64px;height:90px" role="img" aria-label="Engineering tools on workbench"></div>
  <div class="ph ph-dark" style="left:85px;top:40px;width:64px;height:90px" role="img" aria-label="Gear machinery close-up"></div>
  <div class="ph ph-sea" style="left:150px;top:40px;width:64px;height:90px" role="img" aria-label="Auxiliary equipment photograph"></div>
  <div class="ph ph-ind" style="left:215px;top:40px;width:64px;height:90px" role="img" aria-label="Worker in hard hat"></div>
  <div class="abs" style="left:20px;top:80px;width:64px;background:#6b6b6b;color:#fff;font-size:3px;text-align:center;padding:2px 0">ENERGY &amp; ENVIRONMENT</div>
  <div class="abs" style="left:85px;top:80px;width:64px;background:var(--red);color:#fff;font-size:3px;text-align:center;padding:2px 0">ENGINEERING WORKS</div>
  <div class="abs" style="left:150px;top:80px;width:64px;background:#6b6b6b;color:#fff;font-size:3px;text-align:center;padding:2px 0">AUXILIARY EQUIPMENT</div>
  <div class="abs" style="left:215px;top:80px;width:64px;background:var(--red);color:#fff;font-size:3px;text-align:center;padding:2px 0">INDUSTRIAL SERVICE</div>
  <div class="footer"><span class="brand"><i></i>VARRENKO</span><span>varrenko-example.fi</span><span>FRIDAY, DEC 15TH 2017</span></div>
</section>

<section class="slide" style="left:300px;top:840px;background:#262629">
  <div class="ph ph-green" style="left:120px;top:0;width:180px;height:168px" role="img" aria-label="Young plant held in hands"></div>
  <div class="abs" style="left:44px;top:31px;font-size:3px;color:#bbb">Varrenko Groups</div>
  <div class="abs" style="left:44px;top:37px;font-size:8px;font-weight:700;color:#fff">Social Responsibility</div>
  <div class="abs" style="left:44px;top:49px;width:100px;font-size:3px;line-height:1.35;color:#ccc">Varrenko Group's goal is to act in a responsible way as a part of the environment and the community. Acting responsibly towards our interest groups is a central feature of our governance. It has an impact on our procedures and values, and is seen in our everyday work.</div>
  <div class="card" style="left:44px;top:106px;width:68px;height:46px;padding:3px"><svg width="10" height="10"><circle cx="5" cy="5" r="4" fill="none" stroke="#e8403f"/></svg><div class="label" style="font-size:4px">Lorem Ipsum</div><div class="tiny" style="font-size:2.6px">Lorem ipsum dolor sit amet, consectetur adipiscing elit</div></div>
  <div class="card" style="left:116px;top:106px;width:68px;height:46px;padding:3px"><svg width="10" height="10"><rect x="1" y="1" width="8" height="8" fill="none" stroke="#e8403f"/></svg><div class="label" style="font-size:4px">Lorem Ipsum</div><div class="tiny" style="font-size:2.6px">Lorem ipsum dolor sit amet, consectetur adipiscing elit</div></div>
  <div class="card" style="left:188px;top:106px;width:68px;height:46px;padding:3px"><svg width="10" height="10"><circle cx="5" cy="5" r="4" fill="#e8403f"/></svg><div class="label" style="font-size:4px">Lorem Ipsum</div><div class="tiny" style="font-size:2.6px">Lorem ipsum dolor sit amet, consectetur adipiscing elit</div></div>
</section>

<section class="slide" style="left:600px;top:840px">
  <div class="abs h-title" style="left:0;top:14px;width:300px;font-size:6.5px">Our Recent Works</div>
  <div class="abs h-sub" style="left:0;top:22px;width:300px">Your Subtitle Goes Here</div>
  <div class="ph ph-soil" style="left:0;top:40px;width:72px;height:100px" role="img" aria-label="Seedling leaf in soil"></div>
  <div class="abs" style="left:72px;top:40px;width:82px;height:100px;background:var(--red);padding:30px 6px 0;text-align:center;color:#fff">
    <div style="font-size:2.6px">Dolor sit amet</div><div style="font-size:6px;font-weight:700">Environment</div><div style="font-size:2.6px;line-height:1.35;margin-top:2px">Lorem ipsum dolor sit amet, consectetur adipiscing elit, sed do eiusmod tempor incididunt ut labore et dolore magna aliqua.</div>
  </div>
  <div class="ph ph-ind" style="left:155px;top:40px;width:64px;height:100px" role="img" aria-label="Engineer at control panel"></div>
  <div class="ph ph-sea" style="left:220px;top:40px;width:80px;height:48px" role="img" aria-label="Vessel at sea"></div>
  <div class="ph ph-dark" style="left:220px;top:90px;width:80px;height:50px" role="img" aria-label="Industrial plant structure"></div>
  <div class="footer"><span class="brand"><i></i>VARRENKO</span><span>varrenko-example.fi</span><span>FRIDAY, DEC 15TH 2017</span></div>
</section>

<section class="slide" style="left:900px;top:840px">
  <div class="abs h-title" style="left:0;top:14px;width:300px;font-size:6.5px">Our Recent Works</div>
  <div class="abs h-sub" style="left:0;top:22px;width:300px">Your Subtitle Goes Here</div>
  <div class="ph ph-steel" style="left:0;top:40px;width:105px;height:100px" role="img" aria-label="Large industrial machine"></div>
  <div class="abs" style="left:106px;top:40px;width:90px;height:45px;background:var(--red);padding:6px;color:#fff;display:flex;gap:4px">
    <svg width="12" height="12"><circle cx="6" cy="6" r="5" fill="none" stroke="#fff"/></svg>
    <div><div style="font-size:4.4px;font-weight:700">Ownership</div><div style="font-size:2.6px;line-height:1.3">Lorem ipsum dolor sit amet, consectetur adipiscing elit, sed do eiusmod</div></div>
  </div>
  <div class="ph ph-dark" style="left:106px;top:86px;width:90px;height:54px" role="img" aria-label="Welder at work with sparks"></div>
  <div class="abs" style="left:197px;top:40px;width:103px;height:100px;background:var(--ink);padding:24px 8px 0;color:#fff">
    <div style="font-size:2.6px;color:#bbb">Dolor sit amet</div><div style="font-size:7px;font-weight:500">Lorem Ipsum</div>
    <div style="font-size:2.6px;line-height:1.35;color:#ccc;margin-top:3px">Lorem ipsum dolor sit amet, consectetur adipiscing elit, sed do eiusmod tempor incididunt ut labore et dolore magna aliqua.</div>
    <div style="font-size:2.6px;line-height:1.35;color:#ccc;margin-top:3px">Duis aute irure dolor in reprehenderit in voluptate velit esse cillum dolore eu fugiat nulla pariatur.</div>
  </div>
  <div class="footer"><span class="brand"><i></i>VARRENKO</span><span>varrenko-example.fi</span><span>FRIDAY, DEC 15TH 2017</span></div>
</section>

<!-- Row 6 -->
<section class="slide" style="left:0;top:1008px">
  <div class="abs h-title" style="left:0;top:14px;width:300px;font-size:6.5px">Our Recent Works</div>
  <div class="abs h-sub" style="left:0;top:22px;width:300px">Your Subtitle Goes Here</div>
  <div class="ph ph-ind" style="left:33px;top:31px;width:58px;height:52px" role="img" aria-label="Harbour at night"></div>
  <div class="ph ph-steel" style="left:92px;top:31px;width:58px;height:52px" role="img" aria-label="Factory equipment"></div>
  <div class="abs" style="left:151px;top:31px;width:57px;height:52px;background:var(--red);padding:8px 5px;color:#fff"><svg width="10" height="10"><circle cx="5" cy="5" r="4" fill="none" stroke="#fff"/></svg><div style="font-size:4px;font-weight:700">Lorem ipsum</div><div style="font-size:2.5px;line-height:1.3">Lorem ipsum dolor sit amet, consectetur adipiscing elit</div></div>
  <div class="ph ph-sea" style="left:209px;top:31px;width:57px;height:52px" role="img" aria-label="Vessel in waves"></div>
  <div class="abs" style="left:33px;top:84px;width:58px;height:54px;background:var(--ink);padding:12px 5px;color:#fff"><svg width="10" height="10"><circle cx="5" cy="5" r="4" fill="none" stroke="#fff"/></svg><div style="font-size:4px;font-weight:700">Lorem Ipsum</div><div style="font-size:2.5px;line-height:1.3;color:#ccc">Lorem ipsum dolor sit amet, consectetur adipiscing elit</div></div>
  <div class="ph ph-steel" style="left:92px;top:84px;width:58px;height:54px" role="img" aria-label="Engineers reviewing plans"></div>
  <div class="ph ph-sea" style="left:151px;top:84px;width:57px;height:54px" role="img" aria-label="Cargo port"></div>
  <div class="ph ph-dark" style="left:209px;top:84px;width:57px;height:54px" role="img" aria-label="Industrial pipes"></div>
  <div class="footer"><span class="brand"><i></i>VARRENKO</span><span>varrenko-example.fi</span><span>FRIDAY, DEC 15TH 2017</span></div>
</section>

<section class="slide" style="left:300px;top:1008px">
  <div class="abs h-title" style="left:0;top:14px;width:300px;font-size:6.5px">Our Recent Works</div>
  <div class="abs h-sub" style="left:0;top:22px;width:300px">Your Subtitle Goes Here</div>
  <div class="abs" style="left:14px;top:31px;width:76px;height:108px;background:var(--red);padding:16px 8px;color:#fff">
    <div style="font-size:2.6px">Dolor sit amet,</div><div style="font-size:6px;font-weight:700">Social Response</div>
    <div style="font-size:2.6px;line-height:1.35;margin-top:3px">Lorem ipsum dolor sit amet, consectetur adipiscing elit, sed do eiusmod tempor incididunt ut labore et dolore magna aliqua.</div>
    <div style="font-size:2.6px;line-height:1.35;margin-top:3px">Duis aute irure dolor in reprehenderit in voluptate velit esse cillum dolore eu fugiat nulla pariatur. Excepteur sint occaecat cupidatat non proident.</div>
  </div>
  <div class="ph ph-steel" style="left:91px;top:31px;width:54px;height:52px" role="img" aria-label="Factory hall"></div>
  <div class="ph" style="left:146px;top:31px;width:54px;height:52px;background:linear-gradient(135deg,#e9ecef,#9aa5ad)" role="img" aria-label="Machine nameplate"></div>
  <div class="ph ph-ind" style="left:201px;top:31px;width:54px;height:52px" role="img" aria-label="Production line"></div>
  <div class="ph ph-dark" style="left:91px;top:84px;width:81px;height:55px" role="img" aria-label="Gear machinery"></div>
  <div class="ph ph-steel" style="left:173px;top:84px;width:82px;height:55px" role="img" aria-label="Engineers inspecting machinery"></div>
  <div class="footer"><span class="brand"><i></i>VARRENKO</span><span>varrenko-example.fi</span><span>FRIDAY, DEC 15TH 2017</span></div>
</section>

<section class="slide" style="left:600px;top:1008px">
  <div class="abs h-title" style="left:0;top:14px;width:300px;font-size:6.5px">Our Recent Works</div>
  <div class="abs h-sub" style="left:0;top:22px;width:300px">Your Subtitle Goes Here</div>
  <div class="ph ph-steel" style="left:0;top:31px;width:115px;height:52px" role="img" aria-label="Factory floor with machines"></div>
  <div class="abs" style="left:116px;top:31px;width:70px;height:52px;background:var(--red);padding:8px 6px;color:#fff"><div style="font-size:4.6px;font-weight:700">Industry Experts</div><div style="font-size:2.6px;line-height:1.3;margin-top:2px">Lorem ipsum dolor sit amet, consectetur adipiscing elit, sed do eiusmod</div></div>
  <div class="ph ph-ind" style="left:187px;top:31px;width:113px;height:108px" role="img" aria-label="Engineer at industrial plant"></div>
  <div class="abs" style="left:14px;top:97px;font-size:7px;font-weight:700;color:var(--ink)">Industrial Service</div>
  <div class="abs tiny" style="left:14px;top:108px;width:92px;font-size:2.8px">Lorem ipsum dolor sit amet, consectetur adipiscing elit, sed do eiusmod tempor incididunt ut labore et dolore magna aliqua. Ut enim ad minim veniam, quis nostrud exercitation ullamco laboris nisi ut aliquip.</div>
  <div class="ph ph-steel" style="left:120px;top:90px;width:62px;height:45px" role="img" aria-label="Industrial machine unit"></div>
  <div class="footer"><span class="brand"><i></i>VARRENKO</span><span>varrenko-example.fi</span><span>FRIDAY, DEC 15TH 2017</span></div>
</section>

<section class="slide" style="left:900px;top:1008px">
  <div class="abs h-title" style="left:0;top:14px;width:300px;font-size:6.5px">Our Recent Works</div>
  <div class="abs h-sub" style="left:0;top:22px;width:300px">Your Subtitle Goes Here</div>
  <div class="ph ph-dark" style="left:0;top:31px;width:60px;height:54px" role="img" aria-label="Engineers at gear machinery"></div>
  <div class="abs" style="left:60px;top:31px;width:60px;height:54px;background:var(--ink);padding:10px 5px;color:#fff;text-align:center"><svg width="10" height="10"><rect x="1" y="1" width="8" height="8" fill="none" stroke="#fff"/></svg><div style="font-size:4px;font-weight:700">Lorem ipsum</div><div style="font-size:2.5px;line-height:1.3;color:#ccc">Lorem ipsum dolor sit amet, consectetur adipiscing elit</div></div>
  <div class="ph ph-ind" style="left:120px;top:31px;width:60px;height:54px" role="img" aria-label="Offshore platform"></div>
  <div class="abs" style="left:180px;top:31px;width:60px;height:54px;background:var(--ink);padding:10px 5px;color:#fff;text-align:center"><svg width="10" height="10"><circle cx="5" cy="5" r="4" fill="none" stroke="#fff"/></svg><div style="font-size:4px;font-weight:700">Lorem ipsum</div><div style="font-size:2.5px;line-height:1.3;color:#ccc">Lorem ipsum dolor sit amet, consectetur adipiscing elit</div></div>
  <div class="ph ph-steel" style="left:240px;top:31px;width:60px;height:54px" role="img" aria-label="Industrial tower"></div>
  <div class="abs" style="left:0;top:86px;width:60px;height:54px;background:var(--red);padding:10px 5px;color:#fff;text-align:center"><svg width="10" height="10"><circle cx="5" cy="5" r="4" fill="none" stroke="#fff"/></svg><div style="font-size:4px;font-weight:700">Lorem Ipsum</div><div style="font-size:2.5px;line-height:1.3">Lorem ipsum dolor sit amet, consectetur adipiscing elit</div></div>
  <div class="ph ph-ind" style="left:60px;top:86px;width:60px;height:54px" role="img" aria-label="Worker in hard hat"></div>
  <div class="abs" style="left:120px;top:86px;width:60px;height:54px;background:var(--red);padding:10px 5px;color:#fff;text-align:center"><svg width="10" height="10"><rect x="1" y="1" width="8" height="8" fill="none" stroke="#fff"/></svg><div style="font-size:4px;font-weight:700">Lorem ipsum</div><div style="font-size:2.5px;line-height:1.3">Lorem ipsum dolor sit amet, consectetur adipiscing elit</div></div>
  <div class="ph ph-steel" style="left:180px;top:86px;width:60px;height:54px" role="img" aria-label="Engineer at control station"></div>
  <div class="abs" style="left:240px;top:86px;width:60px;height:54px;background:var(--red);padding:10px 5px;color:#fff;text-align:center"><svg width="10" height="10"><polygon points="5,1 9,9 1,9" fill="none" stroke="#fff"/></svg><div style="font-size:4px;font-weight:700">Lorem ipsum</div><div style="font-size:2.5px;line-height:1.3">Lorem ipsum dolor sit amet, consectetur adipiscing elit</div></div>
  <div class="footer"><span class="brand"><i></i>VARRENKO</span><span>varrenko-example.fi</span><span>FRIDAY, DEC 15TH 2017</span></div>
</section>

<div class="strip"></div>
</body>
</html>
```